Coffee pack for specialty coffee roasters

Tres Lunas is a premium brand of specialty coffee roasters based in Prague in the Czech Republic.
We sell coffee beans to other coffee shops (wholesale channel) or to final consumers in our own coffee shops (retail)
We are roasting only specialty grade coffee that we source either directly or through specialty coffee merchants.
We have usually 6-8 coffees on our offer list. Each coffee stays with us 2-7 months based on their harvest season.
We pack our coffee for retail purposes in 250g bags that we sell in our cafés, roastery and clients.
We are now changing our bags from side gusset bags with valve closed by tin ties to flat bottom bags with zipper and valve.
We want evolution of our packaging design (not revolution)
Our current bags are decorated by front and back stickers.
New bags will be custom printed with general information and logo (e.g. Manufacturer information, contact, size etc.) and we want to have paper sleeve with customizable information (e.g. Name of the Coffee origin, farmer, taste profile, farm info etc.)

Target Market(s)

Men + woman aged 25-45, socioeconomical group A and B, university educated, interested in quality products, they care about what they drink and eat.

Industry/Entity Type

Coffee Shop

Font styles to use
Other font styles liked:
• Platform regular

Requirements
Must have
• Design of the pack itself and design of paper sleeve that will be excheangable (we need to change name of the coffee and information about it on the paper sleeve)
Nice to have
• nice to have- coffee related design on the bag under the sleeve
Should not have
• any crazy colours (the bag is golden with only black print on it) and sleeve can be colourful but nothing extravagant.

```html
<!DOCTYPE html>
<html lang="cs">
<head>
<meta charset="utf-8">
<title>Tres Lunas – 250g coffee bag and sleeve</title>
<link href="https://fonts.googleapis.com/css2?family=Josefin+Sans:wght@300;400&family=Oswald:wght@600&family=Roboto+Condensed:wght@300;400&display=swap" rel="stylesheet">
<style>
:root{
  --ink:#111;
  --paper:#fff;
  --line:#d9d9d9;
  --accent:#d21f26;
  --gold-light:#f3dc9c;
  --gold:#e2b867;
  --gold-deep:#c98a3c;
  --fold:#b58a4a;
  --sketch:#e6e6e6;
  --bean:#8a5a32;
  --ocean:#dfe6ee;
}
*{box-sizing:border-box;margin:0;padding:0}
html,body{width:1200px;height:800px;overflow:hidden;background:var(--paper)}
body{position:relative;font-family:"Roboto Condensed",sans-serif;color:var(--ink)}
.abs{position:absolute}
.display{font-family:"Josefin Sans",sans-serif;font-weight:300}

/* ---------- sleeve ---------- */
.sleeve{position:absolute;width:792px;height:188px;background:var(--paper);box-shadow:0 0 6px rgba(0,0,0,.18);overflow:hidden}
.sleeve-front{left:378px;top:20px}
.sleeve-back{left:378px;top:225px}
.roast-date{left:43px;top:8px;font-size:14px}
.taste-hex{left:18px;top:84px;width:104px;height:92px}
.origin-band{left:139px;top:0;width:47px;height:188px;background:var(--ink)}
.origin-name{position:absolute;left:50%;top:50%;transform:translate(-50%,-50%) rotate(90deg);font-family:"Oswald",sans-serif;font-weight:600;font-size:38px;color:var(--paper);letter-spacing:1px;white-space:nowrap}
.map-art{left:186px;top:10px;width:78px;height:150px;background:linear-gradient(160deg,#eee,#d6d6d6);border-radius:30% 50% 40% 60%}
.map-pin{left:192px;top:100px;width:26px;height:26px;border:2px solid var(--accent);border-radius:50%}
.map-pin::after{content:"";position:absolute;left:7px;top:7px;width:8px;height:8px;border-radius:50%;background:var(--accent)}
.flavour{right:401px;top:22px;text-align:right;font-size:18px;line-height:21px;text-transform:uppercase}
.process{right:401px;top:145px;text-align:right;font-size:9px;line-height:11px}
.variety{right:401px;top:172px;font-size:12px;letter-spacing:1px}
.brand{display:flex;flex-direction:column;align-items:center;font-family:"Josefin Sans",sans-serif;font-weight:400;text-transform:uppercase;white-space:nowrap}
.brand .mark{border:3px solid var(--ink);border-radius:50%}
.brand-sleeve{left:418px;top:8px;width:100px;font-size:14px}
.brand-sleeve .mark{width:34px;height:34px;margin-bottom:6px}
.bean-art{left:428px;top:70px;width:78px;height:112px;background:radial-gradient(circle at 50% 40%,#ececec,#d8d8d8);border-radius:40%}
.weight{background:var(--ink);color:var(--paper);text-align:center;border-radius:4px;font-family:"Josefin Sans",sans-serif}
.weight small{display:block;font-size:9px;padding-top:3px}
.weight b{display:block;font-weight:400;font-size:22px;line-height:22px}
.weight-sleeve{left:438px;top:130px;width:60px;height:38px}
.bean-photo{left:543px;top:8px;width:183px;height:54px;border-radius:6px;background:linear-gradient(180deg,#a86f40,#6d4322 60%,#8f5a30)}
.story{left:542px;top:68px;width:184px;font-size:6.2px;line-height:7.3px;text-align:justify}
.brand-small{left:548px;top:154px;width:56px;font-size:7px}
.brand-small .mark{width:18px;height:18px;border-width:2px;margin-bottom:3px}
.maker{border-left:4px solid var(--ink);border-right:4px solid var(--ink);border-radius:4px;padding:2px 6px;font-size:7px;line-height:8px}
.maker .web{font-size:11px;line-height:12px}
.maker .social{font-size:4.5px;display:flex;gap:8px}
.maker .social span::before{content:"";display:inline-block;width:4px;height:4px;border-radius:50%;background:var(--ink);margin-right:2px}
.maker-sleeve{left:614px;top:146px;width:112px}
.cup-art{left:737px;top:10px;width:50px;height:168px;background:linear-gradient(180deg,#e9e9e9,#d9d9d9);border-radius:10px}

/* back sleeve */
.cup-art-back{left:82px;top:18px;width:58px;height:150px;background:linear-gradient(180deg,#e9e9e9,#d5d5d5);border-radius:10px}
.recipe-title{left:148px;top:18px;width:232px;text-align:center;font-size:23px}
.recipe{left:148px;top:58px;width:232px;font-size:7.6px}
.recipe .row{display:flex;border-bottom:1px dashed #444;padding:2px 0 1px;text-transform:uppercase}
.recipe .row span:first-child{width:136px}
.recipe .note{padding-top:2px;border-bottom:1px dashed #444;padding-bottom:3px;line-height:10px}
.brand-back{left:410px;top:20px;width:110px;font-size:15px}
.brand-back .mark{width:40px;height:40px;margin-bottom:8px}
.maker-back{left:410px;top:132px;width:112px}
.globe-label{left:612px;top:4px;color:var(--accent);font-size:21px;font-weight:400}
.globe{left:598px;top:3px;width:180px;height:180px;border-radius:50%;background:radial-gradient(circle at 40% 35%,#f3f6f9,var(--ocean) 70%,#c4cfda)}

/* ---------- bag dieline ---------- */
.dieline{position:absolute;top:430px;width:580px;height:344px;background:linear-gradient(180deg,var(--gold-deep) 0%,var(--gold-light) 30%,var(--gold) 75%,var(--gold-deep) 100%);overflow:hidden}
.dieline::before{content:"";position:absolute;inset:0;background:linear-gradient(90deg,rgba(200,140,60,.35),rgba(255,240,190,.25) 45%,rgba(200,140,60,.35))}
.dieline-a{left:12px}
.dieline-b{left:603px}
.dim-width{position:absolute;top:-2px;left:0;width:100%;text-align:center;font-size:12px}
.dim-width::before,.dim-width::after{content:"";position:absolute;top:8px;width:44%;border-top:1px solid var(--fold)}
.dim-width::before{left:0}.dim-width::after{right:0}
.dim-height{right:0;top:150px;font-size:8px;transform:rotate(90deg);transform-origin:right top}
.fold{position:absolute;top:0;bottom:0;border-left:1px dashed var(--fold)}
.top-margin{left:102px;top:8px;width:1px;height:26px;background:var(--ink);font-size:6px}
.top-margin span{position:absolute;left:4px;top:6px;white-space:nowrap}
.zipper-lines{left:102px;top:50px;width:188px;height:12px;border-top:1px dashed var(--accent);border-bottom:1px dashed var(--accent)}
.zipper-lines::before{content:"";position:absolute;left:0;right:0;top:4px;border-top:1px dashed var(--accent)}
.zipper-label{left:102px;top:48px;width:188px;text-align:center;font-size:12px;background:transparent}
.zipper-label span{background:var(--gold-light);padding:0 4px}
.brand-bag{left:136px;top:90px;width:120px;font-size:17px}
.brand-bag .mark{width:48px;height:48px;margin-bottom:10px}
.bag-art{left:140px;top:186px;width:104px;height:104px;background:radial-gradient(circle at 45% 50%,rgba(60,40,20,.45),rgba(60,40,20,.12) 70%,transparent);border-radius:40%}
.weight-bag{left:447px;top:108px;width:56px;height:34px}
.weight-bag b{font-size:19px;line-height:19px}
.bag-text{left:393px;top:164px;width:168px;font-size:5.4px;line-height:6.6px;text-align:justify}
.maker-bag{left:406px;top:238px;width:142px;font-size:7.4px;line-height:8.6px}
.maker-bag .web{font-size:12px;line-height:13px}
.best-before{left:392px;top:290px;width:176px;text-align:center;font-size:6.4px;line-height:7px}
.best-before small{display:block;font-size:4px}
.sleeve-on-bag{left:0;top:172px;transform:scale(.73);transform-origin:left top;box-shadow:none}
</style>
</head>
<body>

<!-- sleeve front -->
<section class="sleeve sleeve-front" aria-label="Sleeve front">
  <div class="abs roast-date">Praženo:</div>
  <svg class="abs taste-hex" viewBox="-52 -46 104 92" role="img" aria-label="Taste profile hexagon">
    <polygon points="0,0 -25,-43.3 25,-43.3" fill="#2aa7e0"/>
    <polygon points="0,0 25,-43.3 50,0" fill="#3bbf5a"/>
    <polygon points="0,0 50,0 25,43.3" fill="#7a3fae"/>
    <polygon points="0,0 25,43.3 -25,43.3" fill="#d63384"/>
    <polygon points="0,0 -25,43.3 -50,0" fill="#f07c24"/>
    <polygon points="0,0 -50,0 -25,-43.3" fill="#c6d32c"/>
    <polygon points="17,0 8.5,14.7 -8.5,14.7 -17,0 -8.5,-14.7 8.5,-14.7" fill="#fff"/>
    <g font-family="Roboto Condensed,sans-serif" font-size="4" fill="#fff" text-anchor="middle">
      <text x="0" y="-31">AROMA</text><text x="29" y="-15">KYSELOST</text>
      <text x="29" y="18">HORKOST</text><text x="0" y="35">SLADKOST</text>
      <text x="-29" y="18">DOCHUŤ</text><text x="-29" y="-15">TĚLO</text>
    </g>
    <g font-family="Roboto Condensed,sans-serif" font-size="4" fill="#444" text-anchor="middle">
      <text x="0" y="-8">10</text><text x="8" y="-3">7</text><text x="8" y="7">5</text>
      <text x="0" y="12">8</text><text x="-8" y="7">6</text><text x="-8" y="-3">6</text>
    </g>
  </svg>
  <div class="abs origin-band"><span class="origin-name">EKVÁDOR</span></div>
  <div class="abs map-art" role="img" aria-label="Sketch of South America with coffee beans"></div>
  <div class="abs map-pin"></div>
  <div class="abs flavour display">Lískové ořechy<br>Mléčná čokoláda<br>Karamel</div>
  <div class="abs process">zpracování: promyté<br>oblast:PICHINCHA</div>
  <div class="abs variety">100% ARABICA CATURRA</div>
  <div class="abs brand brand-sleeve"><span class="mark"></span>Tres Lunas</div>
  <div class="abs bean-art" role="img" aria-label="Sketch of coffee beans"></div>
  <div class="abs weight weight-sleeve"><small>Hmotnost:</small><b>250g</b></div>
  <div class="abs bean-photo" role="img" aria-label="Photo of roasted coffee beans"></div>
  <p class="abs story">Jsme velmi hrdí, že tato káva se prezentuje v naší pražírně již počtvrté. V ruce držíte čerstvou sklizeň odrůdy caturra a pacas. Tato káva roste ve výšce kolem 1700 metrů nad mořem na svazích sopky Pichincha ve specifické biodiverzní oblasti mezi pralesem a Andami. Sklizeň této kávy probíhala mezi červencem a říjnem 2016 a byla sbírána výhradně ručně. Rok od roku také vidíme zlepšující se třídění a balení kávy. Kvalita je jednoduše hlavní prioritou farmáře Tomáse Veraze.</p>
  <div class="abs brand brand-small"><span class="mark"></span>Tres Lunas</div>
  <div class="abs maker maker-sleeve">Výrobce: Tres Lunas s.r.o.<br><span style="font-size:5px">Květná 214/12, 130 00, Praha 3, ČR</span><div class="web">www.tres-lunas.cz</div><div class="social"><span>/prazimetreslunas</span><span>@tlroastery</span></div></div>
  <div class="abs cup-art" role="img" aria-label="Sketch of coffee pouring into a cup"></div>
</section>

<!-- sleeve back -->
<section class="sleeve sleeve-back" aria-label="Sleeve back">
  <div class="abs cup-art-back" role="img" aria-label="Sketch of a cup, portafilter and beans"></div>
  <h2 class="abs recipe-title display">BREWING RECIPE</h2>
  <div class="abs recipe">
    <div class="row"><span>Gramáž kávy do portafilteru</span><span>18g</span></div>
    <div class="row"><span>Cílová hmotnost espressa</span><span>40g (extrakční poměr 45%)</span></div>
    <div class="row"><span>Celkový čas extrakce</span><span>28 sekund</span></div>
    <div class="note">CHUŤOVÝ PROJEV ESPRESSA:<br>Ekvádor je na espressu krásně vybalancovaný s vůní pralinek a medu. V chuti se pak projevuje převážně chuť čokolády a másla s jemnou oříškovou dochutí. Díky tomu se hodí i na přípravu cappuccina a dalších mléčných variací.</div>
  </div>
  <div class="abs brand brand-back"><span class="mark"></span>Tres Lunas</div>
  <div class="abs maker maker-back">Výrobce: Tres Lunas s.r.o.<br><span style="font-size:5px">Květná 214/12, 130 00, Praha 3, ČR</span><div class="web">www.tres-lunas.cz</div><div class="social"><span>/prazimetreslunas</span><span>@tlroastery</span></div></div>
  <div class="abs globe" role="img" aria-label="Globe showing the Americas with Ecuador marked"></div>
  <svg class="abs" style="left:600px;top:20px" width="120" height="110" viewBox="0 0 120 110">
    <line x1="12" y1="10" x2="100" y2="92" stroke="var(--accent)" stroke-width="1.2" stroke-dasharray="3 2"/>
    <circle cx="100" cy="92" r="4" fill="var(--accent)"/>
  </svg>
  <div class="abs globe-label">Ekvádor</div>
</section>

<!-- bag without sleeve -->
<section class="dieline dieline-a" aria-label="Bag print layout">
  <div class="dim-width">370mm</div>
  <div class="abs dim-height">195mm</div>
  <div class="fold" style="left:102px"></div><div class="fold" style="left:290px"></div><div class="fold" style="left:392px"></div>
  <div class="abs top-margin"><span>15mm</span></div>
  <div class="abs zipper-lines"></div>
  <div class="abs zipper-label"><span>ZIPPER</span></div>
  <div class="abs brand brand-bag"><span class="mark"></span>Tres Lunas</div>
  <div class="abs bag-art" role="img" aria-label="Sketch of a coffee cup with beans forming a continent"></div>
  <div class="abs weight weight-bag"><small>Hmotnost:</small><b>250g</b></div>
  <p class="abs bag-text">V ruce držíte čerstvě praženou zrnkovou kávu. Pracujeme výhradně s výběrovými jednodruhovými arabikami, které získali 85+ bodů. Káva se sbírá na farmách ručně a my navazujeme co nejpřímější, někdy i zcela osobní vazby na farmy. To vše, abychom vám mohli přinášet to nejlepší, co se z aktuálních sklizní nabízet dá a podporovat přitom farmáře, kteří odvádí na svých farmách velmi tvrdou práci.</p>
  <div class="abs maker maker-bag">Výrobce: Tres Lunas s.r.o.<br><span style="font-size:6px">Květná 214/12, 130 00, Praha 3, ČR</span><div class="web">www.tres-lunas.cz</div><div class="social"><span>/prazimetreslunas</span><span>@tlroastery</span></div></div>
  <div class="abs best-before">Nejlepší chuti dosáhnete do 30 dní od pražení kávy.<small>Minimální trvanlivost 90 dní od data pražení uvedeného na zadní straně obalu.</small></div>
</section>

<!-- bag with sleeve -->
<section class="dieline dieline-b" aria-label="Bag print layout with sleeve">
  <div class="dim-width">370mm</div>
  <div class="abs dim-height">195mm</div>
  <div class="fold" style="left:102px"></div><div class="fold" style="left:290px"></div><div class="fold" style="left:392px"></div>
  <div class="abs top-margin"><span>15mm</span></div>
  <div class="abs zipper-lines"></div>
  <div class="abs zipper-label"><span>ZIPPER</span></div>
  <div class="abs brand brand-bag"><span class="mark"></span>Tres Lunas</div>
  <div class="abs weight weight-bag"><small>Hmotnost:</small><b>250g</b></div>

  <div class="sleeve sleeve-on-bag">
    <div class="abs roast-date">Praženo:</div>
    <svg class="abs taste-hex" viewBox="-52 -46 104 92" role="img" aria-label="Taste profile hexagon">
      <polygon points="0,0 -25,-43.3 25,-43.3" fill="#2aa7e0"/>
      <polygon points="0,0 25,-43.3 50,0" fill="#3bbf5a"/>
      <polygon points="0,0 50,0 25,43.3" fill="#7a3fae"/>
      <polygon points="0,0 25,43.3 -25,43.3" fill="#d63384"/>
      <polygon points="0,0 -25,43.3 -50,0" fill="#f07c24"/>
      <polygon points="0,0 -50,0 -25,-43.3" fill="#c6d32c"/>
      <polygon points="17,0 8.5,14.7 -8.5,14.7 -17,0 -8.5,-14.7 8.5,-14.7" fill="#fff"/>
      <g font-family="Roboto Condensed,sans-serif" font-size="4" fill="#fff" text-anchor="middle">
        <text x="0" y="-31">AROMA</text><text x="29" y="-15">KYSELOST</text>
        <text x="29" y="18">HORKOST</text><text x="0" y="35">SLADKOST</text>
        <text x="-29" y="18">DOCHUŤ</text><text x="-29" y="-15">TĚLO</text>
      </g>
    </svg>
    <div class="abs origin-band"><span class="origin-name">EKVÁDOR</span></div>
    <div class="abs map-art" role="img" aria-label="Sketch of South America with coffee beans"></div>
    <div class="abs map-pin"></div>
    <div class="abs flavour display">Lískové ořechy<br>Mléčná čokoláda<br>Karamel</div>
    <div class="abs process">zpracování: promyté<br>oblast:PICHINCHA</div>
    <div class="abs variety">100% ARABICA CATURRA</div>
    <div class="abs brand brand-sleeve"><span class="mark"></span>Tres Lunas</div>
    <div class="abs bean-art" role="img" aria-label="Sketch of coffee beans"></div>
    <div class="abs weight weight-sleeve"><small>Hmotnost:</small><b>250g</b></div>
    <div class="abs bean-photo" role="img" aria-label="Photo of roasted coffee beans"></div>
    <p class="abs story">Jsme velmi hrdí, že tato káva se prezentuje v naší pražírně již počtvrté. V ruce držíte čerstvou sklizeň odrůdy caturra a pacas. Tato káva roste ve výšce kolem 1700 metrů nad mořem na svazích sopky Pichincha ve specifické biodiverzní oblasti mezi pralesem a Andami. Sklizeň této kávy probíhala mezi červencem a říjnem 2016 a byla sbírána výhradně ručně. Rok od roku také vidíme zlepšující se třídění a balení kávy. Kvalita je jednoduše hlavní prioritou farmáře Tomáse Veraze.</p>
    <div class="abs brand brand-small"><span class="mark"></span>Tres Lunas</div>
    <div class="abs maker maker-sleeve">Výrobce: Tres Lunas s.r.o.<br><span style="font-size:5px">Květná 214/12, 130 00, Praha 3, ČR</span><div class="web">www.tres-lunas.cz</div><div class="social"><span>/prazimetreslunas</span><span>@tlroastery</span></div></div>
    <div class="abs cup-art" role="img" aria-label="Sketch of coffee pouring into a cup"></div>
  </div>
</section>

</body>
</html>
```